Law firm website marketed direct to many individual clients

I need someone to design a very basic website for a law firm that will be very eye catching. It's going to be a single-paged, scrolling website with a small number of folds. I have uploaded a simple word document that outlines the basics of what I thought could be the layout, but I am open to suggestion on font, size, shades of color, organization, etc. etc. Essentially the website just needs to be a very efficient and visually appealing way of conveying some simple messages.

Target Market(s)

High volumes of individuals who have gotten into a car accident and then google on their phones a lawyer to hire to represent them.

Industry/Entity Type

Legal

Number of Pages Required

1 page

Font styles to use
Serif
Sans Serif

Colors
34a7d7
85cae6
0592cd

Requirements
Must have
• Must be bright and grab the users attention with color scheme and layout. The different sections should be done in such a way that they can fit entirely onto one smart phone or tablet screen.
Nice to have
• I'd like to try and see what it looks like if in the middle somewhere there is a fold that says "MEET YOUR ATTORNEYS" and includes individual photos of two attorneys, one on the left side and one on the right. And then a small bio section on them. I don't want the photos to include a square or rectangle background, I want the person in the photo to be superimposed on top of whatever pattern or background you have in the fold.
Should not have
• Do not want too much text. Anything more than 2 sentences in any single place is unacceptable.

```html
<!DOCTYPE html>
<html lang="en">
<head>
<meta charset="utf-8">
<title>Meridian Law Group</title>
<link href="https://fonts.googleapis.com/css2?family=Noto+Serif:wght@400;700&family=Open+Sans:wght@400&family=Roboto:wght@400;500;700&family=Roboto+Slab:wght@300;400;500;700&display=swap" rel="stylesheet">
<style>
  :root {
    --brand-blue: #1b8fcf;
    --deep-navy: #0f5478;
    --heading-teal: #0e5a80;
    --panel-dark: #05577a;
    --panel-bright: #0592cd;
    --hero-top: #4f8fb8;
    --hero-bottom: #2d6f9c;
    --ink: #222222;
    --white: #ffffff;
    --header-bg: #fbfbf9;
  }
  * { margin: 0; padding: 0; box-sizing: border-box; }
  html, body { width: 750px; height: 1200px; overflow: hidden; background: var(--white); }
  .page { position: relative; width: 750px; height: 1200px; overflow: hidden; }

  .site-header {
    position: absolute; top: 0; left: 0; width: 750px; height: 61px;
    background: var(--header-bg);
    display: flex; justify-content: space-between; align-items: center;
    padding: 0 36px 0 22px;
    font-family: 'Roboto', sans-serif; font-weight: 500; font-size: 25px;
    color: var(--brand-blue);
  }

  .hero { position: absolute; top: 61px; left: 0; width: 750px; height: 279px; }
  .hero-backdrop {
    position: absolute; inset: 0;
    background: linear-gradient(160deg, var(--hero-top) 0%, #6aa6cc 45%, var(--hero-bottom) 100%);
  }
  .hero-content {
    position: relative; text-align: center; color: var(--white);
    font-family: 'Roboto Slab', serif; font-weight: 500;
  }
  .hero-title { position: absolute; top: 29px; left: 0; width: 750px; font-size: 30px; letter-spacing: 6px; font-weight: 500; }
  .hero-line { position: absolute; left: 0; width: 750px; font-size: 23px; line-height: 28px; }
  .hero-case { top: 87px; }
  .hero-money { top: 126px; }
  .hero-call { top: 184px; }
  .hero-more { top: 223px; }

  .features {
    position: absolute; top: 359px; left: 0; width: 750px; text-align: center;
    font-family: 'Roboto Slab', serif;
  }
  .feature { margin-bottom: 23px; }
  .feature-title { color: var(--heading-teal); font-weight: 500; font-size: 20px; line-height: 24px; }
  .feature-text { color: var(--ink); font-weight: 300; font-size: 20px; line-height: 23.5px; }

  .attorneys { position: absolute; top: 684px; left: 0; width: 750px; height: 291px; }
  .attorney-photo { position: absolute; top: 10px; height: 281px; border-radius: 60px 60px 0 0; }
  .attorney-photo-left { left: 20px; width: 138px; background: linear-gradient(180deg, #d8cfc6 0%, #8e8075 55%, #6d6259 100%); }
  .attorney-photo-right { left: 600px; width: 136px; background: linear-gradient(180deg, #d6c7ba 0%, #3d4e7a 50%, #2c3a63 100%); }
  .attorney-bio { position: absolute; top: 20px; width: 204px; text-align: center; }
  .attorney-bio-left { left: 168px; }
  .attorney-bio-right { left: 392px; }
  .attorney-name { font-family: 'Noto Serif', serif; font-weight: 700; font-size: 17px; line-height: 22px; color: var(--heading-teal); margin-bottom: 18px; }
  .attorney-text { font-family: 'Open Sans', sans-serif; font-size: 13.5px; line-height: 19.5px; color: var(--ink); }
  .attorneys-heading {
    position: absolute; top: 164px; left: 0; width: 750px; text-align: center;
    font-family: 'Noto Serif', serif; font-weight: 700; font-size: 16px; letter-spacing: 8px; color: var(--deep-navy);
  }

  .info-panels { position: absolute; top: 975px; left: 0; width: 750px; height: 187px; display: flex; }
  .info-panel { color: var(--white); text-align: center; font-family: 'Roboto', sans-serif; }
  .info-panel-fee { width: 383px; background: var(--panel-dark); padding-top: 32px; }
  .info-panel-help { width: 367px; background: var(--panel-bright); padding-top: 18px; }
  .info-title { font-weight: 500; font-size: 17.5px; }
  .info-panel-fee .info-title { margin-bottom: 30px; }
  .info-panel-help .info-title { margin-bottom: 8px; }
  .info-text { font-weight: 700; font-size: 12.5px; line-height: 20.5px; }
  .info-panel-fee .info-text { line-height: 24px; }

  .footer-call {
    position: absolute; top: 1162px; left: 0; width: 750px; height: 38px;
    text-align: center; line-height: 38px;
    font-family: 'Roboto', sans-serif; font-weight: 500; font-size: 26px; color: var(--brand-blue);
  }
</style>
</head>
<body>
<div class="page">
  <header class="site-header">
    <span class="brand-name">MERIDIAN LAW GROUP</span>
    <span class="header-phone">504-555-0142</span>
  </header>

  <section class="hero">
    <div class="hero-backdrop" role="img" aria-label="Blue-tinted photo of scales of justice in a courtroom"></div>
    <div class="hero-content">
      <h1 class="hero-title">ACCIDENT? INJURED?</h1>
      <p class="hero-line hero-case">YOUR CASE</p>
      <p class="hero-line hero-money">YOUR MONEY</p>
      <p class="hero-line hero-call">CALL 504-555-0142</p>
      <p class="hero-line hero-more">Learn More</p>
    </div>
  </section>

  <section class="features">
    <div class="feature">
      <h2 class="feature-title">LOW FEES</h2>
      <p class="feature-text">We charge less, so you keep more.</p>
    </div>
    <div class="feature">
      <h2 class="feature-title">FREE CONSULTATION</h2>
      <p class="feature-text">It's always free to talk to us.</p>
    </div>
    <div class="feature">
      <h2 class="feature-title">GET STARTED USING ONLY YOUR PHONE</h2>
      <p class="feature-text">No need to come to the office, sign up<br>using your phone.</p>
    </div>
    <div class="feature">
      <h2 class="feature-title">SPEAK DIRECTLY TO A LAWYER</h2>
      <p class="feature-text">No staff screening. Talk right to a lawyer<br>on your first call.</p>
    </div>
  </section>

  <section class="attorneys">
    <div class="attorney-photo attorney-photo-left" role="img" aria-label="Cut-out photo of attorney in a grey suit holding a folder"></div>
    <div class="attorney-photo attorney-photo-right" role="img" aria-label="Cut-out photo of attorney in a navy pinstripe suit with arms crossed"></div>
    <div class="attorney-bio attorney-bio-left">
      <h3 class="attorney-name">Daniel Reyes</h3>
      <p class="attorney-text">Ut wisi enim ad minim<br>veniam nostrud exerci tation<br>ullamcorper suscipit bortis<br>nisl ut aliquip consequat.</p>
    </div>
    <div class="attorney-bio attorney-bio-right">
      <h3 class="attorney-name">Thomas Walker</h3>
      <p class="attorney-text">Ut wisi enim ad minim<br>veniam nostrud exerci tation<br>ullamcorper suscipit bortis<br>nisl ut aliquip consequat.</p>
    </div>
    <h2 class="attorneys-heading">MEET YOUR ATTORNEYS</h2>
  </section>

  <section class="info-panels">
    <div class="info-panel info-panel-fee">
      <h2 class="info-title">NO FEE UNLESS WE WIN</h2>
      <p class="info-text">We don't get paid unless you get paid.<br>It's as simple as that.<br>We let our results do the talking for us.</p>
    </div>
    <div class="info-panel info-panel-help">
      <h2 class="info-title">QUESTIONS ABOUT ANYTHING?</h2>
      <p class="info-text">We're here to help.<br>Feel free to call us at 504-555-0142<br>to speak to one of our attorneys.<br>With extensive experience<br>in helping clients get the results<br>that they want, our team is always just a phone call away.</p>
    </div>
  </section>

  <footer class="footer-call">CALL 504-555-0142</footer>
</div>
</body>
</html>
```